Flyer for the Lumen 2025 Conference

I am looking to produce a flyer for our upcoming conference, Lumen 2025. This is an annual conference that we plan to publicize on social media. The ideal designer will create a flyer that is eye-catching and effectively communicates the key information. Please see attached our logo, speaker photo, and flyer content.

Target Market(s)

All demographics

Industry/Entity Type

Christian

Font styles to use
Sans Serif

Requirements
Should not have
• Cross, church

```html
<!DOCTYPE html>
<html lang="en">
<head>
<meta charset="utf-8">
<title>Lumen 2025 – A Prophetic Conference</title>
<link rel="stylesheet" href="https://fonts.googleapis.com/css2?family=Anton&family=Arimo:wght@400;700&display=swap">
<style>
  :root {
    --navy: #0d3559;
    --orange: #f5931f;
    --white: #ffffff;
    --ink: #111111;
    --outline-grey: #c9d3dc;
    --page-bg: #e6e6e6;
  }
  html, body {
    margin: 0;
    padding: 0;
    width: 1200px;
    height: 1200px;
    overflow: hidden;
    background: var(--page-bg);
  }
  .flyer {
    position: absolute;
    left: 226px;
    top: 72px;
    width: 596px;
    height: 844px;
    transform: scale(1.25);
    transform-origin: 0 0;
    background: var(--white);
    overflow: hidden;
    font-family: "Arimo", Arial, sans-serif;
  }
  .flyer-shapes {
    position: absolute;
    inset: 0;
    width: 596px;
    height: 844px;
  }
  .title-text {
    font-family: "Anton", "Impact", sans-serif;
  }
  .tagline {
    font-family: "Arimo", Arial, sans-serif;
  }
  .details {
    position: absolute;
    left: 115px;
    top: 483px;
    color: var(--white);
  }
  .detail-row {
    position: absolute;
    left: 0;
    white-space: nowrap;
  }
  .detail-label {
    position: absolute;
    left: 0;
    top: 0;
    font-size: 17px;
    font-weight: 700;
  }
  .detail-value {
    position: absolute;
    left: 126px;
    font-size: 11px;
    line-height: 14.5px;
  }
  .brand-mark {
    position: absolute;
    left: 448px;
    top: 460px;
    display: flex;
    align-items: center;
    gap: 6px;
    color: var(--white);
    font-size: 26px;
    font-weight: 400;
    letter-spacing: 1px;
  }
  .brand-dot {
    width: 14px;
    height: 14px;
    border-radius: 50%;
    background: var(--orange);
  }
  .app-note {
    position: absolute;
    left: 132px;
    top: 687px;
    display: flex;
    align-items: center;
    gap: 10px;
    color: var(--white);
    font-size: 11px;
    white-space: nowrap;
  }
  .download-pill {
    display: inline-block;
    width: 80px;
    height: 19px;
    line-height: 19px;
    border-radius: 10px;
    background: var(--white);
    color: var(--navy);
    text-align: center;
    font-size: 11px;
  }
  .contact-line {
    position: absolute;
    left: 0;
    right: 0;
    top: 794px;
    margin: 0;
    text-align: center;
    color: var(--navy);
    font-size: 16px;
    line-height: 18px;
  }
</style>
</head>
<body>
  <main class="flyer">
    <svg class="flyer-shapes" viewBox="0 0 596 844" role="img" aria-label="Lumen 2025 – A Prophetic Conference">
      <defs>
        <filter id="title-shadow" x="-10%" y="-10%" width="130%" height="130%">
          <feDropShadow dx="3" dy="4" stdDeviation="3" flood-color="#9aa4ad" flood-opacity="0.6"/>
        </filter>
      </defs>

      <polygon class="banner-orange" points="90,388 596,306 596,378 27,473 72,415" fill="var(--orange)"/>
      <polygon class="panel-navy" points="0,484 596,384 596,630 519,714 0,787" fill="var(--navy)"/>
      <polyline class="panel-rule" points="215,444 232,452 596,392" fill="none" stroke="var(--white)" stroke-width="4"/>
      <polygon class="footer-orange" points="0,798 525,723 596,646 596,844 0,844" fill="var(--orange)"/>

      <g class="title-text" filter="url(#title-shadow)">
        <text class="title-name" x="59" y="212" transform="rotate(-5.6 59 212)" font-size="132" fill="var(--orange)" stroke="var(--outline-grey)" stroke-width="12" paint-order="stroke" stroke-linejoin="round" textLength="376" lengthAdjust="spacingAndGlyphs">LUMEN</text>
        <text class="title-year" x="106" y="342" transform="rotate(-5.6 106 342)" font-size="196" fill="var(--navy)" stroke="var(--outline-grey)" stroke-width="14" paint-order="stroke" stroke-linejoin="round" textLength="414" lengthAdjust="spacingAndGlyphs">2025</text>
      </g>

      <text class="tagline" x="77" y="437" transform="rotate(-7.7 77 437)" font-size="40" fill="var(--ink)" textLength="468" lengthAdjust="spacingAndGlyphs">A Prophetic Conference</text>
    </svg>

    <div class="brand-mark"><span class="brand-dot"></span>KAVELO</div>

    <section class="details">
      <div class="detail-row" style="top:0">
        <span class="detail-label">Topic:</span>
        <span class="detail-value" style="top:5px">The Voice Of The Lord</span>
      </div>
      <div class="detail-row" style="top:29px">
        <span class="detail-label">Speaker:</span>
        <span class="detail-value" style="top:5px">Prophet Samuel Odera</span>
      </div>
      <div class="detail-row" style="top:66px">
        <span class="detail-label">Date/Time</span>
        <span class="detail-value" style="top:-6px">Friday, December 26th, 6:30PM - 9:00PM<br>Saturday, December 27th, 5:30PM - 8:00PM<br>Sunday, December 29th, 4:30PM - 7:00PM</span>
      </div>
      <div class="detail-row" style="top:127px">
        <span class="detail-label">Location</span>
        <span class="detail-value" style="top:-6px">The Harborview Performing Arts Center<br>218 Millbrook Avenue<br>Harborview, Maine 04000</span>
      </div>
    </section>

    <div class="app-note">
      <span class="download-pill">Download &#9662;</span>
      <span>the KAVELO App to stay updated on the event</span>
    </div>

    <p class="contact-line">207 555 0142 | contact@kavelo.org | www.kavelo.org</p>
  </main>
</body>
</html>
```